German Webagency needs fresh modern Design

Our website is 4 years old. We need an fresh modern website. All pics we used before are from customers or handmade by us. the new website should be clear with nice handling. please dont copy something from template websites. it would be great if you can surprise us with something great. its our first project here. don´t worry if i make a mistake in responding or briefing. after 20 years you can´t see the works of your own "designer" so we hope for help :-)
our existing site: www.tovankreativ.de
Target Market(s)
small and middle sized companys in germany
Number of Pages Required
4 page
Font styles to use
Colors
Designer to choose colors to be used in the design.
Requirements
Must have
- Responsive (sure we code it)
- Modern and big Font ..Headlines and Slider
- innovative..if you know something new..feel free to show
Nice to have
- the site with our works/refences should look great and later easy to handle when we code it or use wp.
- we like black and grey but if you have better ideas also feel free
Should not have
- a cup of coffe..laptop.. a pencil a handwritten font
- dont copy and modify templates from know websites..bad style

```html
<!DOCTYPE html>
<html lang="en">
<head>
<meta charset="utf-8">
<title>Tovan Kreativ</title>
<link href="https://fonts.googleapis.com/css2?family=Montserrat:wght@300;400;500;600;700&display=swap" rel="stylesheet">
<style>
:root{
  --ink:#222428;
  --text:#555a60;
  --muted:#8a8f96;
  --accent:#4a8fd6;
  --light:#f2f3f5;
  --white:#ffffff;
  --footer:#333436;
  --footer-line:#4a4b4e;
}
*{box-sizing:border-box;margin:0;padding:0}
html,body{width:1200px;height:3261px;overflow:hidden}
body{font-family:'Montserrat',sans-serif;color:var(--text);background:var(--white);position:relative}
section,header,footer{position:relative;width:1200px;overflow:hidden}

/* hero */
.hero{height:660px}
.hero-photo{position:absolute;inset:0;background:linear-gradient(135deg,#3b3a38 0%,#55524c 35%,#2d2f33 65%,#1e1f22 100%)}
.hero-photo::after{content:"";position:absolute;inset:0;background:rgba(0,0,0,.35)}
.brand{position:absolute;left:150px;top:28px;display:flex;align-items:center;gap:10px;color:var(--white);font-weight:700;font-size:30px;letter-spacing:-.5px}
.brand-dot{width:16px;height:16px;border-radius:50%;background:var(--accent)}
.nav{position:absolute;right:298px;top:40px;display:flex;gap:22px;font-size:10.5px;color:var(--white);letter-spacing:.3px;white-space:nowrap}
.nav-cta{position:absolute;left:925px;top:31px;width:127px;height:30px;border:1.5px solid var(--white);color:var(--white);font-size:10.5px;display:flex;align-items:center;justify-content:center;letter-spacing:.3px}
.hero-title{position:absolute;top:258px;width:100%;text-align:center;color:var(--white);font-size:62px;font-weight:500;letter-spacing:-.5px}
.hero-lead{position:absolute;top:343px;left:250px;width:700px;text-align:center;color:#e6e6e6;font-size:13px;line-height:24px;font-weight:300}
.hero-arrow{position:absolute;left:585px;top:612px}

/* headings */
.section-title{position:absolute;width:100%;text-align:center;color:var(--ink);font-size:22px;font-weight:500;letter-spacing:.6px}

/* services */
.services{height:435px;background:var(--white)}
.service{position:absolute;top:95px;width:220px;text-align:center}
.service-photo{width:114px;height:114px;border-radius:50%;margin:0 auto;border:3px solid #e8e8e8}
.service-kicker{margin-top:22px;color:var(--accent);font-size:11.5px;font-weight:300}
.service-name{margin-top:2px;color:var(--ink);font-size:14.5px;font-weight:500;letter-spacing:.5px}
.service-text{margin:14px auto 0;width:180px;font-size:10px;line-height:19px;color:var(--muted);font-weight:300}
.btn-outline{margin:22px auto 0;width:126px;height:26px;border:1px solid #cfd2d6;font-size:7.5px;color:var(--muted);display:flex;align-items:center;justify-content:center;letter-spacing:.4px}

/* testimonials */
.testimonials{height:480px;background:var(--light)}
.quote-mark{position:absolute;font-size:240px;line-height:1;color:var(--white);font-family:Georgia,serif}
.review{position:absolute;width:240px}
.review-head{display:flex;align-items:center;gap:12px}
.avatar{width:60px;height:60px;border-radius:50%;flex:none}
.review-name{font-size:13px;color:var(--ink);letter-spacing:.4px}
.review-role{font-size:10.5px;color:var(--muted);margin-top:2px}
.review-text{margin-top:14px;font-size:9.5px;line-height:17px;color:var(--text);font-weight:300}

/* work */
.work{height:525px;background:var(--white)}
.work-grid{position:absolute;left:224px;top:100px;display:grid;grid-template-columns:repeat(4,180px);grid-template-rows:190px 190px;gap:12px 10px}
.work-item{width:180px;height:190px}
.work-more{background:#1d1d1f;color:var(--white);position:relative}
.work-more span{position:absolute;left:14px;bottom:26px;font-size:15px;font-weight:500;line-height:19px;letter-spacing:.5px}
.work-more svg{position:absolute;right:12px;bottom:28px}

/* partners */
.partners{height:415px;background:var(--white)}
.partner-row{position:absolute;left:0;width:1200px;display:flex;justify-content:center}
.partner{width:170px;height:40px;color:var(--ink);font-weight:700;font-size:17px;display:flex;align-items:center;justify-content:center;gap:8px;white-space:nowrap}
.partner-row.short .partner{width:228px}
.partner i{width:11px;height:11px;background:var(--ink);display:block;flex:none}
.partner b{width:11px;height:11px;border-radius:50%;background:var(--ink);display:block;flex:none}

/* contact */
.contact{height:475px}
.contact-photo{position:absolute;inset:0;background:linear-gradient(180deg,#4f6f93 0%,#5e7f8e 45%,#4d7a5c 100%)}
.contact-photo::after{content:"";position:absolute;inset:0;background:rgba(40,95,170,.45)}
.contact .section-title{color:var(--white)}
.field{position:absolute;background:var(--white);height:34px;font-size:8.5px;color:#9a9ea4;padding:11px 10px}
.field-area{height:146px}
.submit{position:absolute;left:535px;top:410px;width:128px;height:30px;border:1.5px solid var(--white);color:var(--white);font-size:8px;font-weight:600;display:flex;align-items:center;justify-content:center;letter-spacing:.6px}

/* footer */
.footer{height:271px;background:var(--footer);color:#d8d8d8}
.footer-brand{position:absolute;left:150px;top:26px;display:flex;align-items:center;gap:8px;color:var(--white);font-weight:700;font-size:22px}
.footer-brand .brand-dot{width:12px;height:12px}
.contact-row{position:absolute;left:150px;display:flex;align-items:flex-start;gap:22px;font-size:9.5px;line-height:18px}
.contact-row svg{flex:none;margin-top:2px}
.col-title{position:absolute;font-size:9.5px;font-weight:600;color:var(--white);letter-spacing:.4px;padding-bottom:4px;border-bottom:2px solid var(--accent)}
.links{position:absolute;font-size:9.5px;line-height:21px}
.about{position:absolute;left:740px;top:68px;width:310px;font-size:8.5px;line-height:16px;font-weight:300}
.socials{position:absolute;left:740px;top:164px;display:flex;gap:8px}
.socials span{width:20px;height:20px;border-radius:50%;background:var(--white)}
.copyright{position:absolute;left:0;top:226px;width:100%;border-top:1px solid var(--footer-line);padding-top:14px;text-align:center;font-size:7.5px;color:#a5a7aa;letter-spacing:.3px}
</style>
</head>
<body>

<header class="hero">
  <div class="hero-photo" role="img" aria-label="Photo of a film crew with camera and boom microphone at an outdoor shoot"></div>
  <div class="brand"><span class="brand-dot"></span>Tovan Kreativ</div>
  <nav class="nav"><span>HOME</span><span>SERVICES</span><span>PORTFOLIO</span><span>ABOUT US</span></nav>
  <div class="nav-cta">GET IN TOUCH</div>
  <h1 class="hero-title">We are Tovan Kreativ</h1>
  <p class="hero-lead">Tovan Kreativ is a full service web agency who specialise in responsive web design, web development, digital marketing and graphic design. We believe in creating lasting impressions and optimising your business.</p>
  <svg class="hero-arrow" width="30" height="16" viewBox="0 0 30 16"><polyline points="2,2 15,14 28,2" fill="none" stroke="#fff" stroke-width="2"/></svg>
</header>

<section class="services">
  <h2 class="section-title" style="top:45px">WHAT WE CAN DO FOR YOU</h2>
  <div class="service" style="left:230px">
    <div class="service-photo" role="img" aria-label="Photo of a desk with a monitor showing a website layout" style="background:linear-gradient(135deg,#c9ccd2,#5a6270)"></div>
    <div class="service-kicker">Results driven</div>
    <div class="service-name">WEBSITE DESIGN</div>
    <p class="service-text">We build responsive websites that not only look great but are optimised for your business.</p>
    <div class="btn-outline">FIND OUT MORE</div>
  </div>
  <div class="service" style="left:490px">
    <div class="service-photo" role="img" aria-label="Photo of a person sketching marketing plans on a whiteboard" style="background:linear-gradient(135deg,#e6e4df,#a7a39b)"></div>
    <div class="service-kicker">Well researched</div>
    <div class="service-name">DIGITAL MARKETING</div>
    <p class="service-text">We develop and implement well researched marketing strategies to deliver traffic where you need it most.</p>
    <div class="btn-outline">FIND OUT MORE</div>
  </div>
  <div class="service" style="left:750px">
    <div class="service-photo" role="img" aria-label="Photo of a designer working at a screen" style="background:linear-gradient(135deg,#d9c9b8,#7b5a43)"></div>
    <div class="service-kicker">Beautiful</div>
    <div class="service-name">GRAPHIC DESIGN</div>
    <p class="service-text">We design stunning logos, graphics, presentations and almost any other graphic you need to stand out.</p>
    <div class="btn-outline">FIND OUT MORE</div>
  </div>
</section>

<section class="testimonials">
  <div class="quote-mark" style="left:140px;top:40px">&ldquo;</div>
  <div class="quote-mark" style="left:920px;top:280px">&rdquo;</div>
  <h2 class="section-title" style="top:32px">WHAT OUR CLIENTS HAVE TO SAY</h2>

  <div class="review" style="left:226px;top:96px">
    <div class="review-head"><div class="avatar" role="img" aria-label="Portrait of client" style="background:#b59a86"></div><div><div class="review-name">NORA ALBERS</div><div class="review-role">Albers Farben</div></div></div>
    <p class="review-text">Working with the team was easy from day one. They listened closely, delivered a clean new website on time and our enquiries have grown every month since the launch went live.</p>
  </div>
  <div class="review" style="left:485px;top:96px">
    <div class="review-head"><div class="avatar" role="img" aria-label="Portrait of client" style="background:#8a6a55"></div><div><div class="review-name">TIM ROHDE</div><div class="review-role">www.timrohde.de</div></div></div>
    <p class="review-text">Clear communication, fair pricing and strong ideas. Our online shop now loads fast and looks great on every phone, and our customers tell us so nearly every single week.</p>
  </div>
  <div class="review" style="left:744px;top:96px">
    <div class="review-head"><div class="avatar" role="img" aria-label="Portrait of client" style="background:#5f6b4f"></div><div><div class="review-name">FELIX HAHN</div><div class="review-role">Hahn Immobilien</div></div></div>
    <p class="review-text">They rebuilt our property listings site and made it simple to update ourselves. Friendly people who always answer quickly and explain technical matters in plain words.</p>
  </div>
  <div class="review" style="left:226px;top:285px">
    <div class="review-head"><div class="avatar" role="img" aria-label="Portrait of client" style="background:#4a3a36"></div><div><div class="review-name">CLARA WEISS</div><div class="review-role">www.weisslogistik.de</div></div></div>
    <p class="review-text">The new campaign brought more traffic than we had hoped for. Every step was planned well and the reports show exactly which channels work best for our delivery business.</p>
  </div>
  <div class="review" style="left:485px;top:285px">
    <div class="review-head"><div class="avatar" role="img" aria-label="Portrait of client" style="background:#a08a78"></div><div><div class="review-name">PAUL MEYER</div><div class="review-role">Nordwerk</div></div></div>
    <p class="review-text">A reliable partner for design and development. They understood our goals quickly and turned them into a site that our whole team is proud to share.</p>
  </div>
  <div class="review" style="left:744px;top:285px">
    <div class="review-head"><div class="avatar" role="img" aria-label="Portrait of client" style="background:#5b3f44"></div><div><div class="review-name">JULIA SOMMER</div><div class="review-role">Sommer Studio</div></div></div>
    <p class="review-text">Great eye for detail. Our brochures, logo refresh and website now share one clear look, and the process felt relaxed and well organised from start to finish.</p>
  </div>
</section>

<section class="work">
  <h2 class="section-title" style="top:42px">SOME OF OUR WORK</h2>
  <div class="work-grid">
    <div class="work-item" role="img" aria-label="Website project screenshot with blue header and building photos" style="background:linear-gradient(180deg,#e8eef5,#9fb7cf)"></div>
    <div class="work-item" role="img" aria-label="Website project screenshot with green bar and house photo" style="background:linear-gradient(180deg,#e9efe6,#a9b59e)"></div>
    <div class="work-item" role="img" aria-label="Website project screenshot for a transport company" style="background:linear-gradient(180deg,#f0f1ee,#8ea08b)"></div>
    <div class="work-item" role="img" aria-label="Dark website project screenshot with product boxes" style="background:linear-gradient(180deg,#2b2b2d,#101012)"></div>
    <div class="work-item" role="img" aria-label="Purple cosmetics website project screenshot" style="background:linear-gradient(160deg,#6a2a78,#3b1446)"></div>
    <div class="work-item" role="img" aria-label="Yellow website project screenshot with people photo" style="background:linear-gradient(180deg,#e6d23a,#8e8a6a)"></div>
    <div class="work-item" role="img" aria-label="Dark cosmetics website project screenshot with portrait" style="background:linear-gradient(160deg,#3a3436,#0f0d0e)"></div>
    <div class="work-item work-more"><span>VIEW OUR<br>PORTFOLIO</span><svg width="12" height="22" viewBox="0 0 12 22"><polyline points="2,2 10,11 2,20" fill="none" stroke="#fff" stroke-width="2"/></svg></div>
  </div>
</section>

<section class="partners">
  <h2 class="section-title" style="top:30px">COMPANIES WE HAVE WORKED WITH</h2>
  <div class="partner-row" style="top:112px">
    <div class="partner">Velora</div>
    <div class="partner">Kantor</div>
    <div class="partner"><i></i>Stufenwerk</div>
    <div class="partner">Wohnhaus Ost</div>
    <div class="partner"><b></b>Zahnrad</div>
  </div>
  <div class="partner-row" style="top:228px">
    <div class="partner">Krähe &amp; Co</div>
    <div class="partner"><i></i>Mondhof</div>
    <div class="partner">Ernst Bauwerk</div>
    <div class="partner">Nordlicht</div>
    <div class="partner">Autohaus Reiter</div>
  </div>
  <div class="partner-row short" style="top:344px">
    <div class="partner">Gamsberg</div>
    <div class="partner">Auetal</div>
    <div class="partner"><b></b>Achtfeld</div>
  </div>
</section>

<section class="contact">
  <div class="contact-photo" role="img" aria-label="Photo of cows grazing on a green alpine meadow under a blue tint"></div>
  <h2 class="section-title" style="top:92px">LET’S WORK TOGETHER</h2>
  <div class="field" style="left:310px;top:155px;width:285px">Your name</div>
  <div class="field" style="left:610px;top:155px;width:280px">Your email</div>
  <div class="field" style="left:310px;top:203px;width:285px">Your number</div>
  <div class="field" style="left:610px;top:203px;width:280px">Your company</div>
  <div class="field field-area" style="left:310px;top:250px;width:580px">What did you have in mind?</div>
  <div class="submit">SUBMIT</div>
</section>

<footer class="footer">
  <div class="footer-brand"><span class="brand-dot"></span>Tovan Kreativ</div>
  <div class="contact-row" style="top:72px">
    <svg width="14" height="16" viewBox="0 0 14 16"><path d="M7 1a5 5 0 0 0-5 5c0 4 5 9 5 9s5-5 5-9a5 5 0 0 0-5-5z" fill="#fff"/><circle cx="7" cy="6" r="2" fill="#333436"/></svg>
    <span>Lindenweg 14, 34117 Kassel Germany</span>
  </div>
  <div class="contact-row" style="top:106px">
    <svg width="14" height="16" viewBox="0 0 14 16"><rect x="3" y="0.5" width="8" height="15" rx="1.5" fill="#fff"/><rect x="4.5" y="2.5" width="5" height="9" fill="#333436"/></svg>
    <span>0561 - 7203980</span>
  </div>
  <div class="contact-row" style="top:140px">
    <svg width="14" height="16" viewBox="0 0 14 16"><rect x="0.5" y="3" width="13" height="10" fill="#fff"/><polyline points="0.5,3 7,9 13.5,3" fill="none" stroke="#333436" stroke-width="1.2"/></svg>
    <span>Jonas Keller j.keller@tovankreativ.de<br>Lena Brandt l.brandt@tovankreativ.de</span>
  </div>

  <div class="col-title" style="left:515px;top:40px">COMPANY</div>
  <div class="links" style="left:515px;top:68px">Home<br>Services<br>Portfolio</div>
  <div class="links" style="left:598px;top:68px">About Us<br>Contact</div>

  <div class="col-title" style="left:740px;top:40px">ABOUT US</div>
  <p class="about">Small team, big ideas. We plan, design and build websites and campaigns for companies across Germany, with clear prices and personal support from the first call onward.</p>
  <div class="socials"><span></span><span></span><span></span><span></span></div>

  <div class="copyright">COPYRIGHT © TOVAN KREATIV 2018. ALL RIGHTS RESERVED</div>
</footer>

</body>
</html>
```